Prominent Trial Lawyer need a Brochure Design for his firm

Harold J. Brantley of The Brantley Law Firm has been successfully trying severe and complex for over 28 years. He holds the largest verdict in the history of South Georgia of $150,000,000.00 before the late Leonard P. Vasquez in the Okefen District of the Southern District of Georgia. He specializes in sever injuries, whether by auto accident, trucking accident or medical malpractice. He is also well know for his successful trial of business disputes and high net-worth Divorces.
Target Market(s)
Persons who need an aggressive, experienced trial lawyer especially for personal injury, but also for other civil and business matters, high end divorde
Industry/Entity Type
Medical
Contact Information for Business Card
Need to use coloring and logo uplaoded
Requirements
Must have
- 1) biography of principal, Harold J. Brantley
- 2) what we do
- 3) specific cases handled, with specific outcomes (will be supplied)

```html
<!DOCTYPE html>
<html lang="en">
<head>
<meta charset="utf-8">
<title>The Brantley Law Firm – Brochure</title>
<link href="https://fonts.googleapis.com/css2?family=Cinzel:wght@400;700&family=Arimo:wght@400&display=swap" rel="stylesheet">
<style>
  :root{
    --red:#ed1c24;
    --black:#0a0a0a;
    --paper:#f2f2f2;
    --ink:#111;
    --white:#fff;
  }
  html,body{margin:0;padding:0;width:1200px;height:900px;overflow:hidden;background:var(--white);}
  .brochure{position:absolute;left:250px;top:180px;width:712px;height:549px;background:var(--paper);overflow:hidden;}
  .edge-band{position:absolute;left:0;width:712px;height:11px;display:flex;}
  .edge-band.top{top:0}
  .edge-band.bottom{bottom:0}
  .edge-band span{display:block;height:100%}
  .seg-red{background:var(--red)}
  .seg-black{background:var(--black)}

  .brand{position:absolute;text-align:center;font-family:"Cinzel",serif;color:var(--ink);}
  .brand .seal{display:block;margin:0 auto;}
  .brand .name{font-weight:700;margin:0;line-height:1.02;}
  .brand .tag{font-family:"Arimo",sans-serif;color:var(--red);margin:0;}

  .brand-cover{left:0;width:235px;top:195px}
  .brand-cover .name{font-size:25px;margin-top:10px}
  .brand-cover .tag{font-size:11.5px;margin-top:1px}

  .brand-back{left:474px;width:238px;top:399px}
  .brand-back .name{font-size:18px;margin-top:8px}
  .brand-back .tag{font-size:8px;margin-top:1px}

  .brand-inline{left:295px;top:35px;display:flex;align-items:center;gap:8px;text-align:left}
  .brand-inline .name{font-size:12px}
  .brand-inline .tag{font-size:5px;margin-top:1px}

  .edge-statement{position:absolute;right:10px;top:32px;text-align:right;font-family:"Cinzel",serif;color:var(--ink);margin:0;}
  .edge-statement .small{font-size:7.2px;line-height:13px;display:block}
  .edge-statement .large{font-size:12px;letter-spacing:.8px;line-height:19px;display:block}

  .section-bar{position:absolute;left:235px;top:108px;width:238px;height:22px;display:flex;font-family:"Cinzel",serif;font-size:15px;color:var(--white);line-height:22px;}
  .section-bar .lead{background:var(--red);width:120px;text-align:right;padding-right:3px;box-sizing:border-box}
  .section-bar .rest{background:var(--black);flex:1;padding-left:3px}

  .practice-list{position:absolute;left:265px;top:178px;margin:0;padding:0;list-style:none;font-family:"Cinzel",serif;font-size:14.5px;color:var(--ink);letter-spacing:.6px;}
  .practice-list li{position:relative;padding-left:21px;height:27px;line-height:18px}
  .practice-list li::before{content:"";position:absolute;left:0;top:5px;width:8px;height:8px;background:var(--black)}

  .photo{position:absolute}
  .photo-office{left:473px;top:108px;width:239px;height:260px;border-top:5px solid var(--black);border-bottom:5px solid var(--black);box-sizing:border-box;
    background:linear-gradient(180deg,#6b6b68 0%,#8a8a86 35%,#4c5a3a 62%,#7a6a55 82%,#4e4a44 100%);}
  .photo-team{top:363px;height:89px;border:3px solid var(--black);box-sizing:border-box}
  .photo-team.one{left:235px;width:120px;background:linear-gradient(180deg,#6a6d72,#2a2b30)}
  .photo-team.two{left:355px;width:118px;background:linear-gradient(180deg,#3a3434,#121012)}

  .contact{position:absolute;left:265px;top:476px;margin:0;padding:0;list-style:none;font-family:"Arimo",sans-serif;font-size:8.6px;color:var(--ink);}
  .contact li{display:flex;align-items:center;gap:5px;height:10.5px}
  .contact svg{display:block}
</style>
</head>
<body>
<div class="brochure">
  <div class="edge-band top"><span class="seg-red" style="width:120px"></span><span class="seg-black" style="width:234px"></span><span class="seg-red" style="width:239px"></span><span class="seg-black" style="width:119px"></span></div>
  <div class="edge-band bottom"><span class="seg-red" style="width:120px"></span><span class="seg-black" style="width:234px"></span><span class="seg-red" style="width:239px"></span><span class="seg-black" style="width:119px"></span></div>

  <div class="brand brand-cover">
    <svg class="seal" width="92" height="92" viewBox="0 0 92 92" aria-hidden="true"><circle cx="46" cy="46" r="40" fill="none" stroke="var(--red)" stroke-width="8"/></svg>
    <p class="name">The Brantley<br>Law Firm</p>
    <p class="tag">TRIAL LAWYER</p>
  </div>

  <div class="brand brand-inline">
    <svg width="45" height="45" viewBox="0 0 45 45" aria-hidden="true"><circle cx="22.5" cy="22.5" r="19.5" fill="none" stroke="var(--red)" stroke-width="4"/></svg>
    <div>
      <p class="name">The Brantley<br>Law Firm</p>
      <p class="tag">TRIAL LAWYER</p>
    </div>
  </div>

  <p class="edge-statement">
    <span class="small">Whether you are against insurance companies,</span>
    <span class="small">large national companies or governments,</span>
    <span class="large">We level the field and</span>
    <span class="large">give you the edge</span>
  </p>

  <div class="section-bar"><span class="lead">AREAS OF</span><span class="rest">PRACTICE</span></div>

  <ul class="practice-list">
    <li>Business Law</li>
    <li>Civil Litigation</li>
    <li>Criminal Defense</li>
    <li>Family Law</li>
    <li>Personal Injury</li>
  </ul>

  <div class="photo photo-office" role="img" aria-label="Photo of the firm's office entrance with steps, railing and shrubs"></div>
  <div class="photo photo-team one" role="img" aria-label="Group photo of the firm's attorneys and staff"></div>
  <div class="photo photo-team two" role="img" aria-label="Group photo of the firm's legal team in dark suits"></div>

  <ul class="contact">
    <li><svg width="7" height="7" viewBox="0 0 7 7"><rect width="7" height="7" fill="var(--red)"/><circle cx="3.5" cy="3" r="1.4" fill="#fff"/></svg>14 Oakline Way, Cedarview, GA 30999</li>
    <li><svg width="7" height="7" viewBox="0 0 7 7"><rect width="7" height="7" fill="var(--red)"/><rect x="2" y="1.5" width="3" height="4" rx=".6" fill="#fff"/></svg>912-555-0LAW</li>
    <li><svg width="7" height="7" viewBox="0 0 7 7"><rect width="7" height="7" fill="var(--red)"/><rect x="1.5" y="2" width="4" height="3" fill="#fff"/></svg>hbrantley@hjblaw.example</li>
  </ul>

  <div class="brand brand-back">
    <svg class="seal" width="64" height="64" viewBox="0 0 64 64" aria-hidden="true"><circle cx="32" cy="32" r="28" fill="none" stroke="var(--red)" stroke-width="6"/></svg>
    <p class="name">The Brantley<br>Law Firm</p>
    <p class="tag">TRIAL LAWYER</p>
  </div>
</div>
</body>
</html>
```